Architectural, Engineering and Design Build

Tavonex4.com
Veteran Disabled Certified company is doing business in Architecture, Engineer and Design build - look simialr websites and come up with design follow following website
https://dorsey-kalbin.example/
https://www.velmonteam.example/
https://www.pirnoqa.example/contract-vehicles/service-disabled-veteran-owned-small-business-sdvosb/
https://www.corbelhubnet.example/about/sdvosb/

Target Market(s)

US - Defense and Federal Government

Industry/Entity Type

Colors
0054AA
0677BA
7BADD7
CADEEF
E8F1F8

Requirements
Must have
• Army, American patriotism , Buildings, construction, architecture, engineering
Nice to have
• I need to attract federal government agencies and Defense

```html
<!DOCTYPE html>
<html lang="en">
<head>
<meta charset="utf-8">
<title>Tavonex4 — Architecture, Engineering &amp; Design Build</title>
<link href="https://fonts.googleapis.com/css2?family=Exo+2:wght@600;700;800&family=Kumbh+Sans:wght@400;500;600;700&display=swap" rel="stylesheet">
<style>
:root{
  --navy:#1c2a68;
  --blue:#0677ba;
  --blue-deep:#0054aa;
  --red:#d8121c;
  --ink:#1b1b1b;
  --muted:#555;
  --grey-bg:#efefef;
  --white:#fff;
  --star:#f4a51c;
}
*{box-sizing:border-box;margin:0;padding:0}
html,body{width:1200px;height:4847px;overflow:hidden}
body{position:relative;font-family:"Kumbh Sans",sans-serif;color:var(--ink);background:var(--white)}
.abs{position:absolute}
.heading{font-family:"Exo 2",sans-serif;font-weight:700;text-transform:uppercase;color:var(--ink)}
.rule{position:absolute;height:3px;width:54px;background:var(--red)}
.btn{position:absolute;display:flex;align-items:center;justify-content:center;border-radius:22px;background:var(--navy);color:var(--white);font-size:12px;font-weight:500}
.body-text{font-size:12px;line-height:23px;color:var(--muted)}
.photo{position:absolute}

/* hero */
.hero{position:absolute;left:0;top:0;width:1200px;height:604px;background:linear-gradient(100deg,#2b2d33 0%,#4a4d55 40%,#6b6f78 70%,#8a8e98 100%)}
.hero-person{position:absolute;left:560px;top:70px;width:420px;height:534px;background:linear-gradient(180deg,#e6e6e6 0%,#c7d84a 55%,#93a0b4 100%);border-radius:160px 160px 0 0;opacity:.85}
.logo{position:absolute;display:flex;align-items:center;gap:8px;font-family:"Exo 2",sans-serif;font-weight:800}
.logo .dot{width:14px;height:14px;border-radius:50%;background:var(--red)}
.nav{position:absolute;top:14px;font-size:15px;color:var(--white)}
.nav-contact{position:absolute;left:937px;top:2px;width:120px;height:41px;background:var(--white);color:var(--blue);display:flex;align-items:center;justify-content:center;font-size:15px}
.hero h1{position:absolute;left:141px;top:183px;width:520px;font-family:"Exo 2",sans-serif;font-weight:700;font-size:29px;line-height:44.5px;color:var(--white);text-transform:uppercase}
.hero .lede{position:absolute;left:141px;top:372px;font-size:17px;color:var(--white);font-weight:500}
.hero .outline{position:absolute;left:143px;top:421px;width:120px;height:42px;border:2px solid var(--white);color:var(--white);display:flex;align-items:center;justify-content:center;font-size:15px}
.slide-btn{position:absolute;top:538px;width:68px;height:66px;display:flex;align-items:center;justify-content:center}

/* cards */
.card{position:absolute;background:var(--white);border-radius:12px;box-shadow:0 4px 14px rgba(0,0,0,.06);text-align:center}
.card-title{font-weight:700;font-size:15px;color:var(--ink)}
.arrow-dot{position:absolute;width:34px;height:34px;border-radius:50%;background:var(--navy);display:flex;align-items:center;justify-content:center}

.badge{position:absolute;top:1908px;width:132px;height:83px;background:var(--white);box-shadow:0 3px 12px rgba(0,0,0,.1);display:flex;align-items:center;justify-content:center}
.badge span{display:block;width:86px;height:40px;border-radius:8px}

.why-card{position:absolute;top:3037px;width:282px;height:190px;background:var(--white);border-radius:10px;box-shadow:0 4px 16px rgba(0,0,0,.08);text-align:center}
.why-icon{position:absolute;left:97px;top:-40px;width:88px;height:88px;border-radius:50%;background:var(--navy);display:flex;align-items:center;justify-content:center}

.review{position:absolute;top:3481px;width:275px;height:244px;background:var(--white);border-radius:8px}
.quote{position:absolute;right:-6px;top:-14px;width:40px;height:40px;border-radius:50%;background:var(--red);display:flex;align-items:center;justify-content:center;color:var(--white);font-family:Georgia,serif;font-size:34px;font-weight:700;line-height:1;padding-top:12px}
.stars{position:absolute;left:22px;top:20px;color:var(--star);font-size:15px;letter-spacing:3px}
.review p{position:absolute;left:22px;top:44px;width:236px;font-size:11.5px;line-height:23px;color:var(--muted)}
.avatar{position:absolute;left:22px;top:171px;width:56px;height:56px;border-radius:50%;background:linear-gradient(135deg,#8a8f7a,#3b4032)}
.reviewer{position:absolute;left:92px;top:190px;font-size:15px;color:var(--ink)}

.footer{position:absolute;left:0;top:4446px;width:1200px;height:348px;background:#f2f2f2}
.foot-h{position:absolute;font-size:15px;font-weight:600;color:var(--ink)}
.foot-link{position:absolute;font-size:11px;color:var(--ink)}
.social{position:absolute;left:969px;display:flex;align-items:center;gap:12px;font-size:12px}
.social i{display:block;width:26px;height:26px;border-radius:50%;border:1.5px solid var(--ink)}
.copy{position:absolute;left:0;top:4794px;width:1200px;height:53px;background:var(--red);color:var(--white);font-size:11px;display:flex;align-items:center;justify-content:center}
</style>
</head>
<body>

<!-- HERO -->
<section class="hero">
  <div class="hero-person" role="img" aria-label="Smiling construction engineer in white hard hat and safety vest giving a thumbs up in front of a high-rise building"></div>
  <div class="logo" style="left:141px;top:10px;font-size:26px;color:var(--white)"><span class="dot"></span>TAVONEX4</div>
  <span class="nav" style="left:521px">Home</span>
  <span class="nav" style="left:600px">About US</span>
  <span class="nav" style="left:702px">Services</span>
  <span class="nav" style="left:800px">Why Choose Us</span>
  <a class="nav-contact">Contact</a>
  <h1>A clear and concise statement highlighting your services for the defense and government sector</h1>
  <p class="lede">Briefly describe your expertise</p>
  <a class="outline">Contact</a>
  <div class="slide-btn" style="left:1065px;background:var(--white)">
    <svg width="16" height="24" viewBox="0 0 16 24"><path d="M12 3 L4 12 L12 21" fill="none" stroke="#333" stroke-width="2.5"/></svg>
  </div>
  <div class="slide-btn" style="left:1133px;background:var(--blue)">
    <svg width="16" height="24" viewBox="0 0 16 24"><path d="M4 3 L12 12 L4 21" fill="none" stroke="#fff" stroke-width="2.5"/></svg>
  </div>
</section>

<!-- ABOUT -->
<section>
  <div class="photo" style="left:141px;top:685px;width:401px;height:399px;border-radius:20px;background:linear-gradient(180deg,#6f9fc4 0%,#c9c6b0 55%,#f0a640 80%,#1d1a16 100%)" role="img" aria-label="Silhouetted workers on steel scaffolding with a concrete bucket hanging from a crane at sunset"></div>
  <h2 class="heading abs" style="left:647px;top:734px;font-size:28px">About Tavonex4</h2>
  <div class="rule" style="left:647px;top:771px;width:32px"></div>
  <p class="body-text abs" style="left:647px;top:793px;width:410px">Lorem ipsum dolor sit amet, consectetur adipiscing elit, sed do eiusmod ut tempor incididunt ut labore et dolore magna aliqua. Ut enim ad minim ex veniam, quis nostrud exercitation ullamco laboris nisi ut aliquip ex ea amet commodo consequat. Duis aute irure dolor in reprehenderit in voluptate velit esse cillum dolore eu fugiat nulla pariatur.</p>
  <p class="body-text abs" style="left:647px;top:917px;width:410px"><b style="color:var(--ink)">Our Mission :</b> Sed ut perspiciatis unde omnis iste natus error sit amet ex ea voluptatem accusantium doloremque laudantium.</p>
  <a class="btn" style="left:647px;top:986px;width:126px;height:43px">Read More</a>
  <div class="abs" style="left:976px;top:1003px;width:117px;height:37px;background:#f3f3f3" role="img" aria-label="Faint wavy line pattern"></div>
</section>

<!-- SERVICES -->
<section class="abs" style="left:0;top:1170px;width:1200px;height:618px;background:var(--grey-bg)">
  <h2 class="heading abs" style="left:0;width:1200px;text-align:center;top:76px;font-size:30px">Our Services</h2>
  <div class="rule" style="left:573px;top:117px"></div>

  <div class="card" style="left:141px;top:151px;width:290px;height:365px">
    <div class="photo" style="left:17px;top:15px;width:256px;height:243px;border-radius:10px;background:linear-gradient(135deg,#e9e9e6,#bfc2c4 60%,#e3b11f)" role="img" aria-label="Hands sketching architectural plans with a pencil next to a hard hat and magnifier"></div>
    <div class="card-title abs" style="left:0;width:290px;top:276px">Architectural</div>
    <p class="body-text abs" style="left:30px;width:230px;top:297px;line-height:19px">Lorem ipsum dolor sit amet, consectetur adipiscing elit.</p>
    <div class="arrow-dot" style="left:128px;top:348px"><svg width="10" height="14"><path d="M2 2 L8 7 L2 12" fill="none" stroke="#fff" stroke-width="2"/></svg></div>
  </div>
  <div class="card" style="left:455px;top:151px;width:288px;height:365px">
    <div class="photo" style="left:16px;top:15px;width:256px;height:243px;border-radius:10px;background:linear-gradient(180deg,#d9dde0,#a3a79a 50%,#c9d43a 75%,#6b6f73)" role="img" aria-label="Engineer in hard hat and safety vest reviewing blueprints on a site"></div>
    <div class="card-title abs" style="left:0;width:288px;top:276px">Engineering Work</div>
    <p class="body-text abs" style="left:29px;width:230px;top:297px;line-height:19px">Lorem ipsum dolor sit amet, consectetur adipiscing elit.</p>
    <div class="arrow-dot" style="left:127px;top:348px"><svg width="10" height="14"><path d="M2 2 L8 7 L2 12" fill="none" stroke="#fff" stroke-width="2"/></svg></div>
  </div>
  <div class="card" style="left:770px;top:151px;width:289px;height:365px">
    <div class="photo" style="left:16px;top:15px;width:257px;height:243px;border-radius:10px;background:linear-gradient(135deg,#8a6a4a,#e8e6e0 45%,#cfcfc8 70%,#6e7a4c)" role="img" aria-label="Designers drafting building plans at a desk"></div>
    <div class="card-title abs" style="left:0;width:289px;top:276px">Design Build</div>
    <p class="body-text abs" style="left:30px;width:230px;top:297px;line-height:19px">Lorem ipsum dolor sit amet, consectetur adipiscing elit.</p>
    <div class="arrow-dot" style="left:127px;top:348px"><svg width="10" height="14"><path d="M2 2 L8 7 L2 12" fill="none" stroke="#fff" stroke-width="2"/></svg></div>
  </div>
</section>

<!-- CERTIFICATIONS -->
<section>
  <h2 class="heading abs" style="left:141px;top:1866px;font-size:31px">Key Industry Certifications</h2>
  <div class="rule" style="left:141px;top:1908px;width:32px"></div>
  <p class="body-text abs" style="left:141px;top:1915px;width:450px">Sed ut perspiciatis unde omnis iste natus error sit voluptatem accusantium doloremque laudantium, totam rem aperiam, eaque ipsa quae ab illo.</p>
  <a class="btn" style="left:141px;top:1987px;width:126px;height:40px">Contact Us</a>
  <div class="badge" style="left:621px"><span style="background:#cadeef"></span></div>
  <div class="badge" style="left:771px"><span style="background:#f2c9cc"></span></div>
  <div class="badge" style="left:924px"><span style="background:#d3d8e8"></span></div>
</section>

<!-- GALLERY -->
<section class="abs" style="left:0;top:2115px;width:1200px;height:696px;background:var(--grey-bg)">
  <h2 class="heading abs" style="left:0;width:1200px;text-align:center;top:78px;font-size:30px">Project Gallery</h2>
  <div class="rule" style="left:573px;top:118px"></div>
  <p class="body-text abs" style="left:0;width:1200px;text-align:center;top:139px">Sed ut perspiciatis unde omnis iste natus error sit voluptatem accusantium doloremque laudantium, totam rem aperiam, eaque ipsa quae ab illo.</p>
  <div class="photo" style="left:141px;top:186px;width:440px;height:247px;border-radius:10px 10px 0 0;background:linear-gradient(160deg,#4d7fb8 0%,#9bb4c4 35%,#e0a93a 65%,#7a5a25 100%)" role="img" aria-label="Building under construction with a tower crane at golden hour"></div>
  <div class="photo" style="left:617px;top:186px;width:440px;height:247px;border-radius:10px 10px 0 0;background:linear-gradient(180deg,#9fb8d0 0%,#c9c8c2 35%,#8a857c 70%,#5c5852 100%)" role="img" aria-label="Historic government building facade with classical columns and a flag"></div>
  <h3 class="abs" style="left:141px;top:447px;width:440px;font-size:15px;line-height:23px;font-weight:700">Lorem Ipsum Is Simply Dummy Text Of The Printing And Typesetting Industry.</h3>
  <h3 class="abs" style="left:617px;top:447px;width:440px;font-size:15px;line-height:23px;font-weight:700">Lorem Ipsum Is Simply Dummy Text Of The Printing And Typesetting Industry.</h3>
  <p class="body-text abs" style="left:141px;top:498px;width:440px">Sed ut perspiciatis unde omnis iste natus error sit voluptatem accusantium doloremque laudantium, totam rem aperiam, eaque ipsa quae ab illo.</p>
  <p class="body-text abs" style="left:617px;top:498px;width:440px">Sed ut perspiciatis unde omnis iste natus error sit voluptatem accusantium doloremque laudantium, totam rem aperiam, eaque ipsa quae ab illo.</p>
  <a class="btn" style="left:512px;top:570px;width:175px;height:39px">Explore More Projects</a>
</section>

<!-- WHY CHOOSE US -->
<section>
  <h2 class="heading abs" style="left:0;width:1200px;text-align:center;top:2888px;font-size:30px">Why Choose Us</h2>
  <div class="rule" style="left:573px;top:2928px"></div>
  <p class="body-text abs" style="left:0;width:1200px;text-align:center;top:2949px">Lorem ipsum dolor sit amet, consectetur adipiscing elit, sed do eiusmod tempor incididunt ut labore et dolore magna aliqua.</p>

  <div class="why-card" style="left:141px">
    <svg class="abs" style="left:87px;top:-50px" width="108" height="108" viewBox="0 0 108 108"><path d="M20 85 A48 48 0 0 0 90 88" fill="none" stroke="var(--red)" stroke-width="2"/></svg>
    <div class="why-icon"><svg width="40" height="40" viewBox="0 0 40 40" fill="none" stroke="#fff" stroke-width="2"><rect x="6" y="8" width="28" height="26"/><path d="M6 16h28M14 8v26M26 8v26"/></svg></div>
    <div class="card-title abs" style="left:0;width:282px;top:83px;font-size:14px;line-height:21px">Veteran-Owned<br>Business</div>
    <p class="body-text abs" style="left:40px;width:202px;top:129px;font-size:11.5px;line-height:19px">Duis aute irure dolor in reprehenderit in voluptate velit esse cillum dolore.</p>
  </div>
  <div class="why-card" style="left:459px">
    <svg class="abs" style="left:87px;top:-50px" width="108" height="108" viewBox="0 0 108 108"><path d="M14 40 A48 48 0 0 0 54 102" fill="none" stroke="var(--red)" stroke-width="2"/></svg>
    <div class="why-icon"><svg width="40" height="40" viewBox="0 0 40 40" fill="none" stroke="#fff" stroke-width="2"><path d="M10 18a10 10 0 0 1 20 0z"/><path d="M8 18h24"/><circle cx="20" cy="25" r="5"/><path d="M10 38c0-6 4-8 10-8s10 2 10 8"/></svg></div>
    <div class="card-title abs" style="left:0;width:282px;top:83px;font-size:14px;line-height:21px">Experience and<br>Expertise</div>
    <p class="body-text abs" style="left:40px;width:202px;top:129px;font-size:11.5px;line-height:19px">Duis aute irure dolor in reprehenderit in voluptate velit esse cillum dolore.</p>
  </div>
  <div class="why-card" style="left:777px">
    <svg class="abs" style="left:87px;top:-50px" width="108" height="108" viewBox="0 0 108 108"><path d="M60 6 A48 48 0 0 1 100 50" fill="none" stroke="var(--red)" stroke-width="2"/></svg>
    <div class="why-icon"><svg width="40" height="40" viewBox="0 0 40 40" fill="none" stroke="#fff" stroke-width="2"><circle cx="20" cy="16" r="10"/><path d="M20 11l1.6 3.4 3.6.4-2.7 2.4.8 3.6-3.3-1.9-3.3 1.9.8-3.6-2.7-2.4 3.6-.4z"/><path d="M14 25l-3 11 5-3 3 4M26 25l3 11-5-3-3 4"/></svg></div>
    <div class="card-title abs" style="left:0;width:282px;top:83px;font-size:14px;line-height:21px">Commitment to<br>Quality</div>
    <p class="body-text abs" style="left:40px;width:202px;top:129px;font-size:11.5px;line-height:19px">Duis aute irure dolor in reprehenderit in voluptate velit esse cillum dolore.</p>
  </div>
</section>

<!-- TESTIMONIALS -->
<section class="abs" style="left:0;top:3313px;width:1200px;height:563px;background:var(--grey-bg)">
  <h2 class="heading abs" style="left:0;width:1200px;text-align:center;top:79px;font-size:30px">What Are People Saying?</h2>
  <div class="rule" style="left:573px;top:119px"></div>
</section>
<div class="review" style="left:141px">
  <div class="quote">&rdquo;</div><div class="stars">★★★★★</div>
  <p>Lorem ipsum dolor sit amet, consectetur adipiscing elit, sed do eiusmod tempor incididunt ut labore et dolore magna aliqua. Ut enim ad minim veniam, quis nostrud exercitation ullamco laboris nisi.</p>
  <div class="avatar" role="img" aria-label="Customer portrait"></div><div class="reviewer">Mark Delaney</div>
</div>
<div class="review" style="left:467px">
  <div class="quote">&rdquo;</div><div class="stars">★★★★★</div>
  <p>Lorem ipsum dolor sit amet, consectetur adipiscing elit, sed do eiusmod tempor incididunt ut labore et dolore magna aliqua. Ut enim ad minim veniam, quis nostrud exercitation ullamco laboris nisi.</p>
  <div class="avatar" role="img" aria-label="Customer portrait"></div><div class="reviewer">Nora Whitfield</div>
</div>
<div class="review" style="left:775px">
  <div class="quote">&rdquo;</div><div class="stars">★★★★★</div>
  <p>Lorem ipsum dolor sit amet, consectetur adipiscing elit, sed do eiusmod tempor incididunt ut labore et dolore magna aliqua. Ut enim ad minim veniam, quis nostrud exercitation ullamco laboris nisi.</p>
  <div class="avatar" role="img" aria-label="Customer portrait"></div><div class="reviewer">Mark Delaney</div>
</div>
<div class="abs" style="left:557px;top:3755px;width:34px;height:34px;border-radius:50%;border:2px solid var(--navy);display:flex;align-items:center;justify-content:center">
  <svg width="16" height="12"><path d="M15 6H2M6 2L2 6l4 4" fill="none" stroke="#1c2a68" stroke-width="2"/></svg>
</div>
<div class="abs" style="left:606px;top:3755px;width:34px;height:34px;border-radius:50%;background:var(--navy);display:flex;align-items:center;justify-content:center">
  <svg width="16" height="12"><path d="M1 6h13M10 2l4 4-4 4" fill="none" stroke="#fff" stroke-width="2"/></svg>
</div>

<!-- CONSULTATION CTA -->
<section>
  <h2 class="abs" style="left:143px;top:4033px;width:460px;font-family:'Exo 2',sans-serif;font-weight:700;font-size:30px;line-height:40px">Lorem Ipsum Dolor Sit Amet, Consectetur Adipiscing Elit</h2>
  <p class="abs" style="left:143px;top:4137px;width:430px;font-size:13px;line-height:24.5px;color:#333">Lorem Ipsum is simply dummy text of the printing and typesetting industry. Lorem Ipsum has been the industry's standard du ever since the 1500s, when an unknown printer took.</p>
  <a class="btn" style="left:143px;top:4232px;width:154px;height:41px">Project Cosultation</a>
  <div class="abs" style="left:474px;top:4295px;width:117px;height:36px;background:#f3f3f3" role="img" aria-label="Faint wavy line pattern"></div>
  <div class="photo" style="left:659px;top:3961px;width:400px;height:399px;border-radius:14px;background:linear-gradient(135deg,#f4f4f4 0%,#e4e4e4 45%,#6e7480 70%,#d9d9d9 100%)" role="img" aria-label="Businessman in a suit on a phone call working at a laptop in a bright office"></div>
</section>

<!-- FOOTER -->
<footer>
  <div class="footer"></div>
  <div class="logo" style="left:141px;top:4583px;font-size:36px;color:var(--navy)"><span class="dot" style="width:20px;height:20px"></span>TAVONEX4</div>

  <div class="foot-h" style="left:459px;top:4519px">Quick Links</div>
  <div class="foot-link" style="left:462px;top:4569px">» &nbsp;Home</div>
  <div class="foot-link" style="left:462px;top:4598px">» &nbsp;About Us</div>
  <div class="foot-link" style="left:462px;top:4626px">» &nbsp;Services</div>
  <div class="foot-link" style="left:462px;top:4654px">» &nbsp;Projects</div>
  <div class="foot-link" style="left:462px;top:4683px">» &nbsp;Contact Us</div>

  <div class="foot-h" style="left:664px;top:4519px">Contact Details</div>
  <svg class="abs" style="left:664px;top:4566px" width="12" height="15" viewBox="0 0 12 15"><path d="M6 0a6 6 0 0 0-6 6c0 4.5 6 9 6 9s6-4.5 6-9a6 6 0 0 0-6-6z" fill="#1b1b1b"/><circle cx="6" cy="6" r="2.2" fill="#f2f2f2"/></svg>
  <div class="foot-link" style="left:686px;top:4565px;line-height:19px">123, Building Name, Street<br>City, State XY 123456</div>
  <svg class="abs" style="left:664px;top:4619px" width="13" height="13" viewBox="0 0 24 24"><path d="M6.6 10.8a15 15 0 0 0 6.6 6.6l2.2-2.2a1 1 0 0 1 1-.25 11.4 11.4 0 0 0 3.6.57 1 1 0 0 1 1 1V20a1 1 0 0 1-1 1A17 17 0 0 1 3 4a1 1 0 0 1 1-1h3.5a1 1 0 0 1 1 1c0 1.25.2 2.45.57 3.6a1 1 0 0 1-.25 1z" fill="#1b1b1b"/></svg>
  <div class="foot-link" style="left:686px;top:4617px;line-height:19px"><b>Phone</b><br>123-456-7890</div>
  <svg class="abs" style="left:664px;top:4672px" width="13" height="10" viewBox="0 0 13 10"><rect width="13" height="10" fill="#1b1b1b"/><path d="M0 0l6.5 5L13 0" fill="none" stroke="#f2f2f2" stroke-width="1.2"/></svg>
  <div class="foot-link" style="left:686px;top:4669px;line-height:19px"><b>Email</b><br>info@tavonex4.com</div>

  <div class="foot-h" style="left:969px;top:4519px">Follow Us</div>
  <div class="social" style="top:4536px"><i></i>Friendloop</div>
  <div class="social" style="top:4576px"><i></i>Chirpline</div>
  <div class="social" style="top:4617px"><i></i>Vidstream</div>
  <div class="social" style="top:4659px"><i></i>Snapframe</div>

  <div class="copy">© 2024 Tavonex4. All Rights Reserved.</div>
</footer>

</body>
</html>
```